Alpforma Banner

Hi boys and girls :)

We have a little project 4u.

We need a banner in 4 sizes :

Leaderboard: 728*90
Wide SkyScraper: 160*600
Medium Rectangle: 300*250
Ribbon (special format): 990*45

Message on banner :

Either our Logo + Immigration, Integration, Naturalization

Or our Logo + Incorporation, Domicile, Secretarial Services

And if space allows for it www.alpforma-example.com as well.

We are looking for a clean design, check our Website for inspiration concerning colors.

```html
<!DOCTYPE html>
<html lang="en">
<head>
<meta charset="utf-8">
<title>Alpforma Banner Set</title>
<link href="https://fonts.googleapis.com/css2?family=Questrial&display=swap" rel="stylesheet">
<style>
  :root {
    --stage: #6e4b33;
    --logo-bg: #ffffff;
    --ink: #2a2a2a;
    --panel-dark: #262626;
    --panel-mid: #3a3a3a;
    --panel-light: #4a4a4a;
    --label: #ffffff;
    --divider: #5a5a5a;
    --edge: #d8d8d8;
  }
  html, body {
    margin: 0;
    width: 1200px;
    height: 827px;
    overflow: hidden;
    background: var(--stage);
    font-family: "Questrial", sans-serif;
  }
  .banner {
    position: absolute;
    display: flex;
    border: 1px solid var(--edge);
    box-sizing: border-box;
    background: var(--panel-dark);
  }
  .banner--vertical { flex-direction: column; }
  .brand {
    background: var(--logo-bg);
    display: flex;
    align-items: center;
    justify-content: center;
    flex: none;
  }
  .brand-name {
    color: var(--ink);
    font-weight: 400;
    letter-spacing: 0.02em;
  }
  .service {
    position: relative;
    flex: 1;
    display: flex;
    align-items: center;
    justify-content: center;
    gap: 10px;
    color: var(--label);
    border-top: 1px solid var(--divider);
    background: linear-gradient(135deg, var(--panel-light), var(--panel-dark) 60%, var(--panel-mid));
  }
  .banner--horizontal .service { border-top: 0; border-left: 1px solid var(--divider); }
  .service--stacked { flex-direction: column; gap: 14px; }
  .plus {
    width: 16px;
    height: 16px;
    background: rgba(0,0,0,0.45);
    color: var(--label);
    font-size: 12px;
    line-height: 16px;
    text-align: center;
    flex: none;
  }
  .service-label { position: relative; }
  .service-row { justify-content: flex-start; padding-left: 20px; gap: 36px; }

  .skyscraper { left: 147px; top: 46px; width: 177px; height: 663px; }
  .skyscraper .brand { height: 163px; }
  .skyscraper .brand-name { font-size: 30px; }
  .skyscraper .service-label { font-size: 24px; }

  .rectangle { left: 344px; top: 311px; width: 332px; height: 277px; }
  .rectangle .brand { height: 117px; }
  .rectangle .brand-name { font-size: 32px; }
  .rectangle .service-label { font-size: 24px; }

  .leaderboard { left: 344px; top: 609px; width: 804px; height: 100px; }
  .leaderboard .brand { width: 204px; }
  .leaderboard .brand-name { font-size: 28px; }
  .leaderboard .service-label { font-size: 24px; }
  .leaderboard .service { padding-top: 6px; }

  .ribbon { left: 55px; top: 730px; width: 1093px; height: 51px; }
  .ribbon .brand { width: 305px; }
  .ribbon .brand-name { font-size: 26px; }
  .ribbon .service-label { font-size: 24px; }
</style>
</head>
<body>

<section class="banner banner--vertical skyscraper" aria-label="Wide skyscraper 160 by 600">
  <div class="brand"><span class="brand-name">Alpforma</span></div>
  <div class="service service--stacked" role="img" aria-label="Photo of Swiss flags along a street"><span class="plus">+</span><span class="service-label">Immigration</span></div>
  <div class="service service--stacked" role="img" aria-label="Photo of a tram departure board"><span class="plus">+</span><span class="service-label">Integration</span></div>
  <div class="service service--stacked" role="img" aria-label="Photo of a flag on a building"><span class="plus">+</span><span class="service-label">Naturalization</span></div>
</section>

<section class="banner banner--vertical rectangle" aria-label="Medium rectangle 300 by 250">
  <div class="brand"><span class="brand-name">Alpforma</span></div>
  <div class="service service-row" role="img" aria-label="Photo of Swiss flags along a street"><span class="plus">+</span><span class="service-label">Immigration</span></div>
  <div class="service service-row" role="img" aria-label="Photo of a tram departure board"><span class="plus">+</span><span class="service-label">Integration</span></div>
  <div class="service service-row" role="img" aria-label="Photo of a flag on a building"><span class="plus">+</span><span class="service-label">Naturalization</span></div>
</section>

<section class="banner banner--horizontal leaderboard" aria-label="Leaderboard 728 by 90">
  <div class="brand"><span class="brand-name">Alpforma</span></div>
  <div class="service service--stacked" role="img" aria-label="Photo of Swiss flags along a street"><span class="plus">+</span><span class="service-label">Immigration</span></div>
  <div class="service service--stacked" role="img" aria-label="Photo of a tram departure board"><span class="plus">+</span><span class="service-label">Integration</span></div>
  <div class="service service--stacked" role="img" aria-label="Photo of a flag on a building"><span class="plus">+</span><span class="service-label">Naturalization</span></div>
</section>

<section class="banner banner--horizontal ribbon" aria-label="Ribbon 990 by 45">
  <div class="brand"><span class="brand-name">Alpforma</span></div>
  <div class="service" role="img" aria-label="Photo of Swiss flags along a street"><span class="plus">+</span><span class="service-label">Immigration</span></div>
  <div class="service" role="img" aria-label="Photo of a tram departure board"><span class="plus">+</span><span class="service-label">Integration</span></div>
  <div class="service" role="img" aria-label="Photo of a flag on a building"><span class="plus">+</span><span class="service-label">Naturalization</span></div>
</section>

</body>
</html>
```